Finally a Vodka produced for women ! (Label Design)

We are a small distillery based in Melbourne, Australia and we need a Vodka label design solution that will appeal to women aged 30-50 years and radiate luxury. Full Details are in a design brief attached. We thank you in advance.

Target Market(s)

Affluent females 30-50 years.

Industry/Entity Type

Spirits/Alcohol

Requirements
Must have
• Be clear this is a luxury Vodka.
Nice to have
• Elegance.

```html
<!DOCTYPE html>
<html lang="en">
<head>
<meta charset="utf-8">
<title>Premium Vodka – Label Options</title>
<link href="https://fonts.googleapis.com/css2?family=Cinzel:wght@400&family=Montserrat:wght@600&family=Oswald:wght@300&display=swap" rel="stylesheet">
<style>
  :root{
    --paper:#ffffff;
    --glass-edge:#9fbad4;
    --glass-mid:#e4ecee;
    --facet:#a9aeb3;
    --pink:#f4b4bf;
    --pink-soft:#f7d3d9;
    --grey-dark:#8b8b8d;
    --grey-mid:#b3b3b5;
    --text-grey:#8e8f92;
    --text-light:#f1f1f1;
  }
  html,body{margin:0;padding:0;overflow:hidden;background:var(--paper);}
  .sheet{width:1200px;height:670px;display:block;}
  .serif{font-family:'Cinzel',serif;}
  .sans{font-family:'Montserrat',sans-serif;font-weight:600;}
  .condensed{font-family:'Oswald',sans-serif;font-weight:300;}
  .facet{fill:none;stroke:var(--facet);stroke-width:3;}
  .facet-thin{fill:none;stroke:#ffffff;stroke-width:1.5;opacity:.7;}
  .option-letter{font-family:'Montserrat',sans-serif;font-weight:600;font-size:56px;fill:#8e8f92;}
</style>
</head>
<body>
<svg class="sheet" viewBox="0 0 2560 1440" preserveAspectRatio="none" xmlns="http://www.w3.org/2000/svg">
  <defs>
    <linearGradient id="glass" x1="0" x2="1" y1="0" y2="0">
      <stop offset="0" stop-color="var(--glass-edge)"/>
      <stop offset=".25" stop-color="#d7e4ec"/>
      <stop offset=".5" stop-color="var(--glass-mid)"/>
      <stop offset=".75" stop-color="#d7e4ec"/>
      <stop offset="1" stop-color="#7f9fbf"/>
    </linearGradient>
    <linearGradient id="pinkFade" x1="0" x2="0" y1="0" y2="1">
      <stop offset="0" stop-color="var(--pink)" stop-opacity=".9"/>
      <stop offset=".7" stop-color="var(--pink-soft)" stop-opacity=".8"/>
      <stop offset="1" stop-color="var(--pink-soft)" stop-opacity=".2"/>
    </linearGradient>
    <linearGradient id="pinkBase" x1="0" x2="1" y1="0" y2="1">
      <stop offset="0" stop-color="var(--pink-soft)"/>
      <stop offset=".6" stop-color="var(--pink)"/>
      <stop offset="1" stop-color="var(--pink-soft)"/>
    </linearGradient>

    <g id="bottle">
      <!-- neck and cap -->
      <rect x="410" y="88" width="158" height="48" rx="6" fill="var(--pink)"/>
      <path d="M415 136 H563 V265 L592 300 H385 L415 265 Z" fill="#eef2f4" stroke="var(--facet)" stroke-width="3"/>
      <path class="facet" d="M438 136 V265 M540 136 V265"/>
      <rect x="447" y="88" width="80" height="212" fill="var(--grey-dark)"/>
      <g class="serif" fill="var(--text-light)" font-size="22" text-anchor="middle">
        <text transform="translate(484 194) rotate(-90)">ROSE QUARTZ</text>
        <text transform="translate(506 194) rotate(-90)">FILTERED</text>
      </g>
      <rect x="385" y="300" width="207" height="18" fill="#b9cde0" stroke="var(--facet)" stroke-width="2"/>
      <!-- body -->
      <path d="M385 318 H592 L800 1030 L700 1250 H280 L178 1030 Z" fill="url(#glass)" stroke="var(--facet)" stroke-width="3"/>
      <path class="facet" d="M415 318 L205 1030 M562 318 L772 1030 M178 1030 H800 M205 1030 L280 1200 M772 1030 L700 1200 M280 1200 H700 M280 1200 L330 1250 M700 1200 L650 1250 M380 1200 L420 1250 M600 1200 L560 1250 M488 1200 V1250 M420 1250 L488 1200 L560 1250"/>
      <!-- decorative artwork -->
      <path role="img" aria-label="Rose quartz watercolour triangle" d="M488 322 L600 600 L520 650 L440 690 L325 720 Z" fill="url(#pinkFade)"/>
      <path class="facet-thin" d="M330 715 L420 780 L520 870 L610 930 M280 830 L420 780 M360 900 L450 850 L540 760 M610 880 L690 780"/>
      <g class="serif" fill="var(--text-grey)" text-anchor="middle">
        <text x="488" y="752" font-size="30" letter-spacing="2">PREMIUM</text>
        <text x="488" y="805" font-size="66" letter-spacing="2">VODKA</text>
      </g>
      <path role="img" aria-label="Rose quartz watercolour wash" d="M265 1035 H780 L540 1195 L330 1110 Z" fill="url(#pinkBase)" opacity=".85"/>
      <path d="M488 895 L585 990 L488 1085 L391 990 Z" fill="var(--pink)"/>
      <g class="condensed" fill="var(--text-grey)" text-anchor="middle">
        <text x="488" y="1128" font-size="34">700ML</text>
        <rect x="433" y="1136" width="110" height="2" fill="var(--text-grey)"/>
        <text x="488" y="1164" font-size="22">40% ALC/VOL</text>
      </g>
    </g>

    <g id="label-text">
      <g class="serif" font-size="21" text-anchor="middle">
        <text x="320" y="988">ROSE QUARTZ</text>
        <text x="320" y="1006">FILTERED</text>
        <text x="657" y="988">HANDCRAFTED</text>
        <text x="657" y="1006">IN AUSTRALIA</text>
      </g>
      <g class="sans" text-anchor="middle">
        <text x="490" y="976" font-size="22" letter-spacing="5">SILVER</text>
        <text x="490" y="1000" font-size="22" letter-spacing="5">WREN</text>
        <text x="490" y="1015" font-size="9" letter-spacing="4">DISTILLERY</text>
      </g>
    </g>
  </defs>

  <!-- Option A -->
  <g class="option option-a">
    <use href="#bottle"/>
    <rect class="band" x="205" y="945" width="567" height="80" fill="var(--grey-dark)"/>
    <rect x="205" y="950" width="567" height="3" fill="#dadada"/>
    <use href="#label-text" fill="var(--text-light)"/>
    <text class="option-letter" x="205" y="1425">A</text>
  </g>

  <!-- Option B -->
  <g class="option option-b" transform="translate(800 0)">
    <use href="#bottle"/>
    <rect class="band" x="205" y="952" width="567" height="72" fill="#ffffff" opacity=".55" stroke="#c8c8c8" stroke-width="2"/>
    <use href="#label-text" fill="#9d9ea1"/>
    <text class="option-letter" x="175" y="1425">B</text>
  </g>

  <!-- Option C -->
  <g class="option option-c" transform="translate(1600 0)">
    <use href="#bottle"/>
    <rect class="band" x="205" y="945" width="567" height="80" fill="var(--grey-mid)" opacity=".9"/>
    <rect x="205" y="950" width="567" height="3" fill="#e4e4e4"/>
    <path d="M488 945 L528 985 L488 1025 L448 985 Z" fill="var(--pink)" opacity=".6"/>
    <use href="#label-text" fill="#f4f4f4"/>
    <text class="option-letter" x="180" y="1425">C</text>
  </g>
</svg>
</body>
</html>
```